Slatebook App Analytics Dashboard Design

Our app is designed for visitors centers and hotel/lodging concierges to assist (and allow) travelers to book tours and activities on-site with a kiosk or at front desk. This analytics dashboard will help the hotels or visitors centers owners and employees to understand the activity within their app for their specific business.

We would like this to be modern, clean and sleek and really stand out when we highlight it at an upcoming presentation/conference. The stats we would like to show are:
(By day/month/time period)
Number of Bookings
Source of Bookings i.e. website vs mobile vs kiosk (% of a whole)
Top 5 tour operators booked (and volume of each)
Top 5 tours booked (and volume of each)
Commissions earned (*admin only option - won't show for regular users)

I am including some screen shots of our current Slatebook app to see our general design and color palate. We would like to use this library: https://quillarch.com/open-source/meridian/gallery

This could lead to further UX design improvements for our current app and future projects. I will be paying out a winner and will provide feedback as the contest goes on.

Target Market(s)

Hotel Concierges & Managers, Visitor Bureau Managers and Employees

Industry/Entity Type

Travel Industry

Font styles to use
Other font styles liked:
• Apple Fonts: San Francisco

Requirements
Must have
• We would like to use this library: https://quillarch.com/open-source/meridian/gallery
• The stats we would like to show are:
• (By day/month/time period)
• Number of Bookings
• Source of Bookings i.e. website vs mobile vs kiosk (% of a whole)
• Top 5 tour operators booked (and volume of each)
• Top 5 tours booked (and volume of each)
• Commissions earned (*admin only option - won't show for regular users)
Nice to have
• Would be nice to have an easy way for users to toggle between time periods that are common and also choose dates from drop down calendars.
• Will be used on an Slatebook and Slatebook Max

```html
<!DOCTYPE html>
<html lang="en">
<head>
<meta charset="utf-8">
<title>Slatebook Analytics Dashboard</title>
<link href="https://fonts.googleapis.com/css2?family=Inter:wght@400;500;600;700&display=swap" rel="stylesheet">
<style>
  :root{
    --device-black:#0a0d0c;
    --sidebar:#0f1614;
    --brand-green:#0db14b;
    --panel:#ffffff;
    --soft-grey:#efefef;
    --text-dark:#1d1d1d;
    --text-mid:#444;
    --sidebar-text:#e6e6e6;
    --ring-track:#dcdcdc;
    --ring-web:#f7941d;
    --ring-mobile:#1e9be9;
    --ring-kiosk:#8e4bd8;
    --ops-top:#17a6f2;
    --ops-bottom:#6a3ed6;
    --tours-top:#f6ac1e;
    --tours-bottom:#e7620f;
    --bar-ops-track:#1d3a8a;
    --bar-tours-track:#9a3d06;
  }
  *{box-sizing:border-box;margin:0;padding:0}
  html,body{width:1200px;height:943px;overflow:hidden}
  body{background:var(--device-black);font-family:"Inter",sans-serif;position:relative;color:var(--text-dark)}

  .status-bar{position:absolute;left:0;top:0;width:1200px;height:26px;color:#fff;font-size:12px;display:flex;align-items:center;justify-content:space-between;padding:0 14px}
  .status-bar .time{position:absolute;left:50%;transform:translateX(-50%);font-weight:500}
  .status-bar .battery{display:flex;align-items:center;gap:6px}
  .battery-icon{width:26px;height:11px;border:1px solid #fff;border-radius:2px;padding:1px}
  .battery-icon span{display:block;height:100%;background:#fff}

  .sidebar{position:absolute;left:0;top:26px;width:106px;height:917px;background:var(--sidebar)}
  .nav-item{display:flex;flex-direction:column;align-items:center;gap:8px;color:var(--sidebar-text);font-size:12px;height:112px;justify-content:center;position:relative}
  .nav-item.active{color:var(--brand-green)}
  .nav-item.active::before{content:"";position:absolute;left:0;top:26px;width:3px;height:50px;background:var(--brand-green)}

  .main{position:absolute;left:110px;top:30px;width:1082px;height:905px;background:var(--panel);border-radius:4px;overflow:hidden}
  .main-header{height:52px;background:var(--brand-green);color:#fff;font-size:18px;font-weight:600;display:flex;align-items:center;justify-content:center}

  .period-toggle{position:absolute;left:18px;top:68px;width:518px;height:34px;display:flex;border:1px solid var(--brand-green);border-radius:3px;overflow:hidden}
  .period-toggle span{flex:1;display:flex;align-items:center;justify-content:center;font-size:14px;color:var(--brand-green)}
  .period-toggle span+span{border-left:1px solid var(--brand-green)}
  .period-toggle .selected{background:var(--brand-green);color:#fff}

  .chart-card{position:absolute;left:14px;top:112px;width:526px;height:350px;border-radius:4px;background:linear-gradient(180deg,#12c98c 0%,#0ab55a 100%)}

  .totals{position:absolute;left:560px;top:78px;width:500px;height:100px;display:flex;align-items:center}
  .total{flex:1;text-align:center}
  .total+.total{border-left:1px solid #ccc}
  .total strong{display:block;font-size:36px;font-weight:600;color:var(--text-dark)}
  .total strong sup{font-size:18px;vertical-align:14px}
  .total small{display:block;font-size:12px;color:var(--text-mid);margin-top:4px;text-transform:uppercase}

  .source-card{position:absolute;left:558px;top:200px;width:510px;height:270px;background:var(--soft-grey);border-radius:4px}
  .source-card h2{font-size:18px;font-weight:500;text-align:center;padding:16px 0 14px;margin:0 18px;border-bottom:1px solid #d5d5d5}
  .rings{display:flex;justify-content:space-around;padding-top:26px}
  .ring{text-align:center;font-size:12px;color:var(--text-mid)}
  .ring svg{display:block;margin-bottom:8px}

  .rank-card{position:absolute;top:490px;width:518px;height:360px;border-radius:4px;color:#fff;padding:0 18px}
  .rank-card.operators{left:14px;background:linear-gradient(180deg,var(--ops-top),var(--ops-bottom))}
  .rank-card.tours{left:552px;top:484px;background:linear-gradient(180deg,var(--tours-top),var(--tours-bottom))}
  .rank-card h2{font-size:19px;font-weight:500;text-align:center;padding:16px 0 14px;border-bottom:1px solid rgba(255,255,255,.35);margin:0 10px 10px}
  .rank-row{display:flex;align-items:center;height:58px}
  .thumb{width:46px;height:46px;border-radius:50%;flex:none;border:2px solid rgba(255,255,255,.7)}
  .rank-name{font-size:18px;margin-left:12px;width:220px;white-space:nowrap;flex:none}
  .bar-track{width:150px;height:10px;border-radius:5px;margin-left:10px;flex:none}
  .operators .bar-track{background:var(--bar-ops-track)}
  .tours .bar-track{background:var(--bar-tours-track)}
  .bar-fill{height:100%;border-radius:5px;background:#fff}
  .rank-pct{font-size:13px;font-weight:700;margin-left:auto;padding-left:8px}
</style>
</head>
<body>
  <div class="status-bar">
    <span>Slatebook</span>
    <span class="time">4:21 PM</span>
    <span class="battery">100% <span class="battery-icon"><span></span></span></span>
  </div>

  <nav class="sidebar">
    <div class="nav-item active">
      <svg width="42" height="42" viewBox="0 0 42 42" fill="none" stroke="currentColor" stroke-width="3"><circle cx="21" cy="21" r="18"/><path d="M21 24 L26 11" stroke-linecap="round"/><circle cx="21" cy="25" r="2" fill="currentColor"/></svg>
      Dashboard
    </div>
    <div class="nav-item">
      <svg width="42" height="42" viewBox="0 0 42 42" fill="none" stroke="currentColor" stroke-width="2.5"><rect x="5" y="8" width="32" height="30" rx="2"/><path d="M5 15h32M13 4v8M29 4v8"/><g fill="currentColor" stroke="none"><rect x="11" y="20" width="4" height="4"/><rect x="19" y="20" width="4" height="4"/><rect x="27" y="20" width="4" height="4"/><rect x="11" y="28" width="4" height="4"/><rect x="19" y="28" width="4" height="4"/><rect x="27" y="28" width="4" height="4"/></g></svg>
      Events
    </div>
    <div class="nav-item">
      <svg width="42" height="42" viewBox="0 0 42 42" fill="none" stroke="currentColor" stroke-width="2.5"><rect x="5" y="10" width="28" height="26" rx="2"/><path d="M11 20h10M11 26h14M11 31h8"/><path d="M30 4v20l3 4 3-4V4z"/></svg>
      Bookings
    </div>
    <div class="nav-item">
      <svg width="42" height="42" viewBox="0 0 42 42" fill="none" stroke="currentColor" stroke-width="2.5"><circle cx="21" cy="13" r="8"/><path d="M7 38c0-10 6-15 14-15s14 5 14 15z"/></svg>
      Profile
    </div>
    <div class="nav-item">
      <svg width="42" height="42" viewBox="0 0 42 42" fill="none" stroke="currentColor" stroke-width="2.5" stroke-linecap="round"><path d="M8 8l26 26M6 12l6-6"/><path d="M34 8L10 32l-4 4M30 5a6 6 0 0 1 7 7"/></svg>
      Settings
    </div>
  </nav>

  <main class="main">
    <header class="main-header">Dashboard</header>

    <div class="period-toggle">
      <span>Day</span><span class="selected">Month</span><span>Year</span>
    </div>

    <section class="chart-card" aria-label="Bookings over time">
      <svg width="526" height="350" viewBox="0 0 526 350">
        <defs>
          <linearGradient id="areaFill" x1="0" y1="0" x2="0" y2="1">
            <stop offset="0" stop-color="#e4e21d"/>
            <stop offset="1" stop-color="#28c25b"/>
          </linearGradient>
        </defs>
        <g stroke="rgba(255,255,255,.12)" stroke-width="1">
          <line x1="40" y1="20" x2="510" y2="20"/><line x1="40" y1="42" x2="510" y2="42"/><line x1="40" y1="64" x2="510" y2="64"/><line x1="40" y1="86" x2="510" y2="86"/><line x1="40" y1="108" x2="510" y2="108"/><line x1="40" y1="130" x2="510" y2="130"/><line x1="40" y1="152" x2="510" y2="152"/><line x1="40" y1="174" x2="510" y2="174"/><line x1="40" y1="196" x2="510" y2="196"/><line x1="40" y1="218" x2="510" y2="218"/>
        </g>
        <g fill="#fff" font-size="12" font-family="Inter, sans-serif">
          <text x="4" y="24">1000</text><text x="8" y="46">900</text><text x="8" y="68">800</text><text x="8" y="90">700</text><text x="8" y="112">600</text><text x="8" y="134">500</text><text x="8" y="156">400</text><text x="8" y="178">300</text><text x="8" y="200">200</text><text x="10" y="222">100</text>
        </g>
        <path d="M100 185 C150 178 180 170 215 159 C265 140 285 115 330 104 C370 90 405 82 440 82 L440 300 L100 300 Z" fill="url(#areaFill)"/>
        <g fill="#0fbf6e" stroke="#fff" stroke-width="2">
          <circle cx="100" cy="185" r="6"/><circle cx="215" cy="159" r="6"/><circle cx="330" cy="104" r="6"/><circle cx="440" cy="82" r="6"/>
        </g>
        <g fill="none" stroke="#fff" stroke-width="1.6">
          <circle cx="24" cy="322" r="10"/><path d="M29 322h-10m4-4l-4 4 4 4"/>
          <circle cx="492" cy="320" r="10"/><path d="M487 320h10m-4-4l4 4-4 4"/>
        </g>
        <g fill="#fff" font-size="14" font-family="Inter, sans-serif" text-anchor="middle">
          <text x="100" y="327">5 Jun</text><text x="215" y="326">12 Jun</text><text x="330" y="325">19 Jun</text><text x="440" y="324">26 Jun</text>
        </g>
      </svg>
    </section>

    <section class="totals">
      <div class="total"><strong>728</strong><small>No. of bookings</small></div>
      <div class="total"><strong><sup>$</sup>290</strong><small>Commissions received</small></div>
    </section>

    <section class="source-card">
      <h2>SOURCE OF BOOKINGS</h2>
      <div class="rings">
        <div class="ring">
          <svg width="110" height="110" viewBox="0 0 110 110"><circle cx="55" cy="55" r="46" fill="none" stroke="var(--ring-track)" stroke-width="10"/><circle cx="55" cy="55" r="46" fill="none" stroke="var(--ring-web)" stroke-width="10" stroke-dasharray="86.7 289" transform="rotate(-90 55 55)"/><text x="55" y="62" text-anchor="middle" font-size="22" font-weight="600" font-family="Inter, sans-serif" fill="#1d1d1d">30%</text></svg>
          WEBSITE
        </div>
        <div class="ring">
          <svg width="110" height="110" viewBox="0 0 110 110"><circle cx="55" cy="55" r="46" fill="none" stroke="var(--ring-track)" stroke-width="10"/><circle cx="55" cy="55" r="46" fill="none" stroke="var(--ring-mobile)" stroke-width="10" stroke-dasharray="144.5 289" transform="rotate(-90 55 55)"/><text x="55" y="62" text-anchor="middle" font-size="22" font-weight="600" font-family="Inter, sans-serif" fill="#1d1d1d">50%</text></svg>
          MOBILE
        </div>
        <div class="ring">
          <svg width="110" height="110" viewBox="0 0 110 110"><circle cx="55" cy="55" r="46" fill="none" stroke="var(--ring-track)" stroke-width="10"/><circle cx="55" cy="55" r="46" fill="none" stroke="var(--ring-kiosk)" stroke-width="10" stroke-dasharray="57.8 289" transform="rotate(-90 55 55)"/><text x="55" y="62" text-anchor="middle" font-size="22" font-weight="600" font-family="Inter, sans-serif" fill="#1d1d1d">20%</text></svg>
          KIOSK
        </div>
      </div>
    </section>

    <section class="rank-card operators">
      <h2>TOP 5 TOUR OPERATORS BOOKED</h2>
      <div class="rank-row"><div class="thumb" role="img" aria-label="Operator photo" style="background:linear-gradient(135deg,#c9d6e0,#8a9aa8)"></div><span class="rank-name">Dorian Pell</span><div class="bar-track"><div class="bar-fill" style="width:92%"></div></div><span class="rank-pct">92%</span></div>
      <div class="rank-row"><div class="thumb" role="img" aria-label="Operator photo" style="background:linear-gradient(135deg,#6d6d6d,#2b2b2b)"></div><span class="rank-name">Marcus Vane</span><div class="bar-track"><div class="bar-fill" style="width:86%"></div></div><span class="rank-pct">86%</span></div>
      <div class="rank-row"><div class="thumb" role="img" aria-label="Operator photo" style="background:linear-gradient(135deg,#7a6a60,#3a302a)"></div><span class="rank-name">Elliot Strand</span><div class="bar-track"><div class="bar-fill" style="width:74%"></div></div><span class="rank-pct">74%</span></div>
      <div class="rank-row"><div class="thumb" role="img" aria-label="Operator photo" style="background:linear-gradient(135deg,#8a8f7a,#3c4034)"></div><span class="rank-name">Owen Halloway</span><div class="bar-track"><div class="bar-fill" style="width:68%"></div></div><span class="rank-pct">68%</span></div>
      <div class="rank-row"><div class="thumb" role="img" aria-label="Operator photo" style="background:linear-gradient(135deg,#c0392b,#6b2a20)"></div><span class="rank-name">Nadia Brooke</span><div class="bar-track"><div class="bar-fill" style="width:60%"></div></div><span class="rank-pct">60%</span></div>
    </section>

    <section class="rank-card tours">
      <h2>TOP 5 TOURS BOOKED</h2>
      <div class="rank-row"><div class="thumb" role="img" aria-label="Tour photo" style="background:linear-gradient(135deg,#c85a3c,#6e7a8a)"></div><span class="rank-name">Wonder Harbor</span><div class="bar-track"><div class="bar-fill" style="width:92%"></div></div><span class="rank-pct">92%</span></div>
      <div class="rank-row"><div class="thumb" role="img" aria-label="Tour photo" style="background:linear-gradient(135deg,#1f8a4c,#0d4a2a)"></div><span class="rank-name">Silvermist River</span><div class="bar-track"><div class="bar-fill" style="width:86%"></div></div><span class="rank-pct">86%</span></div>
      <div class="rank-row"><div class="thumb" role="img" aria-label="Tour photo" style="background:linear-gradient(135deg,#5ab4e6,#1d5f9a)"></div><span class="rank-name">Coral Bay Aquarium</span><div class="bar-track"><div class="bar-fill" style="width:74%"></div></div><span class="rank-pct">74%</span></div>
      <div class="rank-row"><div class="thumb" role="img" aria-label="Tour photo" style="background:linear-gradient(135deg,#7c8a5a,#4a3a2a)"></div><span class="rank-name">Ridge Adventure Park</span><div class="bar-track"><div class="bar-fill" style="width:68%"></div></div><span class="rank-pct">68%</span></div>
      <div class="rank-row"><div class="thumb" role="img" aria-label="Tour photo" style="background:linear-gradient(135deg,#9fd2f0,#3a88b8)"></div><span class="rank-name">SkyDrift</span><div class="bar-track"><div class="bar-fill" style="width:60%"></div></div><span class="rank-pct">60%</span></div>
    </section>
  </main>
</body>
</html>
```